nutrition company business card

I would like to have a business card that has two sides, one being the green color from the Company name on the logo. I am open to ideas and looks that work with my logo. I like the idea of having a negative image of the tree on the green side.

For my information on the card I must have:
Linda Moorcombe
415-872-6041
lindamoorcombe@quellmail.net

This area will need to be updated once I complete my schooling.

Reason: I need to extend my deadline by one day as I have been sick the last week and not had time to review all the new designs. Thank you.

Industry/Entity Type

Nutrition

Requirements
Must have
• I would like to have a business card that has two sides, one being the green color from the Company name on the logo. I am open to ideas and looks that work with my logo. I like the idea of having a negative image of the tree on the green side.
• For my information on the card I must have:
• Linda Moorcombe
• 415-872-6041
• lindamoorcombe@quellmail.net
• This area will need to be updated once I complete my schooling.

```html
<!DOCTYPE html>
<html lang="en">
<head>
<meta charset="utf-8">
<title>Verdant Table — Business Card</title>
<link href="https://fonts.googleapis.com/css2?family=Quicksand:wght@400;500&family=Open+Sans:wght@400;600&display=swap" rel="stylesheet">
<style>
  :root{
    --leaf:#6cb52d;
    --leaf-deep:#58a020;
    --bark:#9a857a;
    --paper:#ffffff;
    --ink:#4a4a4a;
    --muted:#8a8a8a;
    --rule:#c9c9c9;
    --stage:#ecebe7;
  }
  *{box-sizing:border-box;margin:0;padding:0}
  html,body{width:1200px;height:1024px;overflow:hidden;background:var(--stage)}
  .sheet{position:relative;width:1200px;height:1024px}
  .card{position:absolute;left:250px;width:700px;height:400px;overflow:hidden;
        box-shadow:0 6px 18px rgba(0,0,0,.12)}
  .card--front{top:70px;background:radial-gradient(circle at 40% 30%,#7cc23a,var(--leaf) 55%,var(--leaf-deep))}
  .card--back{top:554px;background:linear-gradient(135deg,#fff,#f1f1f1)}

  .front-brand{position:absolute;left:0;right:0;top:0;bottom:0;display:flex;align-items:center;justify-content:center;gap:28px}
  .brand-dot{width:120px;height:120px;border-radius:50%;border:5px solid var(--paper)}
  .brand-text{color:var(--paper);font-family:'Quicksand',sans-serif}
  .brand-name{font-size:56px;font-weight:400;line-height:1}
  .brand-tag{font-size:26px;font-weight:400;margin-top:8px;opacity:.95}

  .back-swoop{position:absolute;left:0;bottom:0;width:700px;height:400px}
  .back-brand{position:absolute;left:40px;top:58px;display:flex;align-items:center;gap:16px}
  .back-brand .brand-dot{width:66px;height:66px;border:4px solid var(--bark)}
  .back-brand .brand-name{font-family:'Quicksand',sans-serif;font-size:32px;color:var(--leaf);font-weight:400;line-height:1}
  .back-brand .brand-tag{font-family:'Quicksand',sans-serif;font-size:16px;color:var(--muted);margin-top:4px}
  .divider{position:absolute;left:400px;top:60px;width:1px;height:150px;background:var(--rule)}
  .contact{position:absolute;left:430px;top:78px;font-family:'Open Sans',sans-serif;color:var(--ink)}
  .contact-name{font-size:26px;font-weight:600;color:var(--leaf);margin-bottom:22px}
  .contact-line{display:flex;align-items:center;gap:12px;font-size:15px;margin-bottom:12px}
  .contact-line svg{width:16px;height:16px;flex:none}
</style>
</head>
<body>
<main class="sheet">
  <section class="card card--front" aria-label="Card front">
    <div class="front-brand">
      <span class="brand-dot"></span>
      <div class="brand-text">
        <div class="brand-name">Verdant Table</div>
        <div class="brand-tag">healthy eating made easy</div>
      </div>
    </div>
  </section>

  <section class="card card--back" aria-label="Card back">
    <svg class="back-swoop" viewBox="0 0 700 400" aria-hidden="true">
      <path d="M0 170 C120 230 230 300 290 400 L0 400 Z" fill="var(--leaf)"/>
      <path d="M0 225 C110 270 200 330 250 400 L0 400 Z" fill="#fff"/>
      <path d="M0 235 C100 278 185 335 232 400 L0 400 Z" fill="var(--bark)"/>
    </svg>
    <div class="back-brand">
      <span class="brand-dot"></span>
      <div>
        <div class="brand-name">Verdant Table</div>
        <div class="brand-tag">healthy eating made easy</div>
      </div>
    </div>
    <div class="divider"></div>
    <div class="contact">
      <div class="contact-name">Linda Moorcombe</div>
      <div class="contact-line">
        <svg viewBox="0 0 24 24"><path fill="var(--leaf)" d="M6.6 10.8a15.1 15.1 0 0 0 6.6 6.6l2.2-2.2a1 1 0 0 1 1-.25 11.4 11.4 0 0 0 3.6.57 1 1 0 0 1 1 1V20a1 1 0 0 1-1 1A17 17 0 0 1 3 4a1 1 0 0 1 1-1h3.5a1 1 0 0 1 1 1c0 1.25.2 2.45.57 3.57a1 1 0 0 1-.25 1z"/></svg>
        <span>415-872-6041</span>
      </div>
      <div class="contact-line">
        <svg viewBox="0 0 24 24"><rect x="2" y="5" width="20" height="14" rx="2" fill="var(--leaf)"/><path d="M3 6l9 7 9-7" fill="none" stroke="#fff" stroke-width="1.8"/></svg>
        <span>lindamoorcombe@quellmail.net</span>
      </div>
    </div>
  </section>
</main>
</body>
</html>
```